Stonefield Partners Business Card Design

We are looking for a new business card design, we are not happy with our current design. We are a boutique management consulting firm and our clients are typically fortune 500 companies.

I have attached the current front and back that we have as well as a version of our logo that can be used. I am trying to get a higher resolution version of the logo file to upload to the project.

Target Market(s)

Fortune 500 companies are our primary client base. Financial services, life sciences, pharmaceuticals and telecom companies are

Industry/Entity Type

Management Consulting

Contact Information for Business Card

We are trying to communicate a high degree of professionalism, a somewhat minimalist perhaps with some air of whimsy (without overdoing it). Attached is the current design, front and back as well as logos. I like the current back of the card and assume we will keep the phrase the same.

From a color palette perspective, I prefer to stay with a gray scale as they are today.

Font styles to use
Sans Serif

Colors
1b1b1b
474747
ffffff

Requirements
Must have
• Two sided business card design. File format should be something that can be used outside of Photoshop like MS Publisher so that they can be edited with personal information.
• Font should be calibri or something very similar and should be available within MS Office
Should not have
• No other logos or graphics outside of the logo provided.

```html
<!DOCTYPE html>
<html lang="en">
<head>
<meta charset="utf-8">
<title>Stonefield Partners Business Card</title>
<link rel="stylesheet" href="https://fonts.googleapis.com/css2?family=Carlito:wght@400;700&display=swap">
<style>
  :root {
    --ink: #1b1b1b;
    --graphite: #474747;
    --paper: #ffffff;
    --mark-grey: #d9d9d9;
    --backdrop: #9b9b9b;
    --card-font: "Carlito", "Calibri", sans-serif;
  }
  html, body {
    margin: 0;
    padding: 0;
    overflow: hidden;
  }
  body {
    width: 1139px;
    height: 1200px;
    background: var(--backdrop);
    position: relative;
    font-family: var(--card-font);
  }
  .card {
    position: absolute;
    left: 173px;
    width: 804px;
    height: 444px;
    box-shadow: 0 22px 18px -12px rgba(0, 0, 0, 0.45);
    overflow: hidden;
  }

  /* Front */
  .card-front {
    top: 109px;
    background: var(--ink);
    color: var(--paper);
    text-align: center;
  }
  .front-mark {
    position: absolute;
    left: 0;
    right: 0;
    top: 40px;
    display: flex;
    flex-direction: column;
    align-items: center;
    gap: 12px;
  }
  .front-mark .mark-dot {
    width: 84px;
    height: 84px;
    border-radius: 50%;
    background: var(--mark-grey);
  }
  .front-mark .mark-name {
    font-size: 34px;
    font-weight: 700;
    color: var(--mark-grey);
    line-height: 1;
  }
  .tagline {
    position: absolute;
    left: 0;
    right: 0;
    top: 229px;
    margin: 0;
    font-size: 35px;
    font-weight: 400;
    line-height: 47px;
  }
  .website {
    position: absolute;
    left: 0;
    right: 0;
    top: 365px;
    margin: 0;
    font-size: 23px;
    font-weight: 700;
  }

  /* Back */
  .card-back {
    top: 634px;
    background: var(--paper);
    color: var(--ink);
  }
  .brand-band {
    position: absolute;
    left: 0;
    right: 0;
    top: 71px;
    height: 128px;
    background: var(--ink);
  }
  .brand-lockup {
    position: absolute;
    left: 118px;
    top: 16px;
    display: flex;
    align-items: center;
    gap: 22px;
  }
  .brand-lockup .mark-dot {
    width: 84px;
    height: 84px;
    border-radius: 50%;
    background: var(--paper);
  }
  .brand-lockup .mark-name {
    font-size: 104px;
    font-weight: 700;
    color: var(--paper);
    line-height: 96px;
  }
  .foot-band {
    position: absolute;
    left: 0;
    right: 0;
    bottom: 0;
    height: 31px;
    background: var(--ink);
  }
  .contact {
    position: absolute;
    top: 236px;
    margin: 0;
    font-style: normal;
    font-size: 23px;
    line-height: 30px;
    color: var(--ink);
  }
  .contact strong {
    font-weight: 700;
    font-size: 25px;
  }
  .contact-person {
    right: 413px;
    text-align: right;
  }
  .contact-office {
    left: 432px;
    text-align: left;
  }
</style>
</head>
<body>

  <section class="card card-front" aria-label="Card front">
    <div class="front-mark">
      <span class="mark-dot"></span>
      <span class="mark-name">Stonefield</span>
    </div>
    <p class="tagline">The trusted partner<br>for the decisions that matter most</p>
    <p class="website">www.StonefieldPartners.com</p>
  </section>

  <section class="card card-back" aria-label="Card back">
    <div class="brand-band">
      <div class="brand-lockup">
        <span class="mark-dot"></span>
        <span class="mark-name">Stonefield</span>
      </div>
    </div>

    <address class="contact contact-person">
      <strong>Mark Ellison</strong><br>
      Los Angeles Office<br>
      Managing Director<br>
      206.555.0142<br>
      mellison@stonefieldpartners.com
    </address>

    <address class="contact contact-office">
      <strong>Stonefield Partners, Inc.</strong><br>
      Headquarters<br>
      612 Linden Avenue<br>
      Suite 210<br>
      Cedar Bay, WA 98120
    </address>

    <div class="foot-band"></div>
  </section>

</body>
</html>
```